Flyer required for podiatry clinic

DL Size please.
Wanting a design for a mail box flyer for the local area. Wanting to increase our customer base. The information on the attached word document needs to be included.
If stock photos are able to be fit in that would be appreciated
We cater from young children to the elderly so should be suitable for all.

Colors

Designer to choose colors to be used in the design.

```html
<!DOCTYPE html>
<html lang="en">
<head>
<meta charset="utf-8">
<title>Stride Podiatry Flyer</title>
<link rel="stylesheet" href="https://fonts.googleapis.com/css2?family=Open+Sans:wght@400;600;700;800&display=swap">
<style>
:root{
  --navy:#0c3566;
  --blue:#1c6cb3;
  --green:#8cc63f;
  --pale:#e3f1fa;
  --white:#ffffff;
}
*{margin:0;padding:0;box-sizing:border-box}
html,body{width:857px;height:1200px;overflow:hidden;background:var(--white)}
body{font-family:"Open Sans",Arial,sans-serif;color:var(--blue)}
.flyer{position:relative;width:857px;height:1200px;overflow:hidden;background:var(--white)}
.brand{position:absolute;left:40px;top:26px;display:flex;align-items:center;gap:10px;font-weight:800;font-size:34px;color:var(--blue);line-height:1}
.brand-dot{width:18px;height:18px;border-radius:50%;background:var(--green)}
.hero-photo{position:absolute;right:0;top:0;width:440px;height:440px;background:linear-gradient(160deg,#f4f6f8 0%,#d9e3ea 55%,#b9c8d3 100%)}
.foot-photo{position:absolute;right:14px;top:290px;width:250px;height:250px;border-radius:50%;border:8px solid var(--white);background:radial-gradient(circle at 40% 40%,#e9cdb8,#b98f75 70%,#8d6b58)}
.headline{position:absolute;left:40px;top:140px;width:420px;font-weight:800;font-size:25px;line-height:1.18;color:var(--navy)}
.services{position:absolute;left:40px;top:270px;list-style:none;width:390px}
.services li{display:flex;align-items:center;gap:12px;font-weight:700;font-size:18px;color:var(--blue);height:26px;margin-bottom:2px}
.services svg{flex:none}
.locations-band{position:absolute;left:0;top:520px;width:440px;height:680px;background:var(--pale)}
.locations-title{position:absolute;left:40px;top:555px;font-weight:800;font-size:30px;color:var(--navy)}
.location{position:absolute;font-size:15px;line-height:1.35;color:var(--blue)}
.location h3{font-weight:700;font-size:16px;color:var(--navy);margin-bottom:10px}
.location .label{color:var(--green);font-weight:700;display:block}
.location .phone{font-weight:700;color:var(--navy);margin-top:6px;display:block}
.loc-a{left:40px;top:615px;width:190px}
.loc-b{left:240px;top:615px;width:180px;border-left:2px solid var(--green);padding-left:14px}
.loc-c{left:40px;top:820px;width:380px}
.loc-c .row{display:flex;justify-content:space-between}
.fine-print{position:absolute;left:40px;top:1085px;width:360px;font-size:14px;line-height:1.4;color:var(--blue)}
.fine-print strong{display:block;color:var(--navy);font-size:15px;margin-top:4px}
.offer-panel{position:absolute;left:428px;top:400px;width:429px;height:800px}
.offer-panel svg{position:absolute;left:0;top:0}
.offer-title{position:absolute;left:455px;top:560px;font-weight:800;font-size:42px;color:var(--white)}
.offer-intro{position:absolute;left:455px;top:620px;width:370px;font-size:17px;line-height:1.4;color:var(--white)}
.offer-one{position:absolute;left:440px;top:700px;width:355px;height:80px;border-radius:40px;background:var(--green);display:flex;align-items:center;gap:14px;padding:0 18px;color:var(--white)}
.offer-one .tag{font-weight:800;font-size:20px;white-space:nowrap}
.offer-one .text{font-size:15px;line-height:1.25}
.offer-one .price{font-weight:800;font-size:24px}
.offer-two-text{position:absolute;left:480px;top:825px;width:240px;font-size:19px;line-height:1.35;color:var(--white);letter-spacing:.5px}
.offer-two-badge{position:absolute;left:735px;top:808px;width:110px;height:110px;border-radius:50%;background:var(--green);display:flex;align-items:center;justify-content:center;font-weight:800;font-size:20px;color:var(--white)}
.worry{position:absolute;left:455px;top:965px;width:370px;font-size:18px;line-height:1.4;color:var(--white)}
.book{position:absolute;left:455px;top:1105px;width:380px;font-weight:800;font-size:21px;line-height:1.3;color:var(--green)}
</style>
</head>
<body>
<div class="flyer">
  <div class="hero-photo" role="img" aria-label="Smiling podiatrist in a white coat"></div>
  <div class="brand"><span class="brand-dot"></span>Stride Podiatry</div>

  <h1 class="headline">BULK BILLING for GP EPC/ Care plans , DVA Card Holders.ClaimPoint and CardPay available</h1>

  <ul class="services">
    <li><svg width="18" height="18" viewBox="0 0 18 18"><rect width="18" height="18" rx="3" fill="#8cc63f"/><path d="M4 9l3.5 3.5L14 5.5" stroke="#fff" stroke-width="2.4" fill="none"/></svg>Heel Pain- Spurs and Plantar Fasciitis</li>
    <li><svg width="18" height="18" viewBox="0 0 18 18"><rect width="18" height="18" rx="3" fill="#8cc63f"/><path d="M4 9l3.5 3.5L14 5.5" stroke="#fff" stroke-width="2.4" fill="none"/></svg>Orthotics</li>
    <li><svg width="18" height="18" viewBox="0 0 18 18"><rect width="18" height="18" rx="3" fill="#8cc63f"/><path d="M4 9l3.5 3.5L14 5.5" stroke="#fff" stroke-width="2.4" fill="none"/></svg>Fungal Nail Infections (Laser treatment)</li>
    <li><svg width="18" height="18" viewBox="0 0 18 18"><rect width="18" height="18" rx="3" fill="#8cc63f"/><path d="M4 9l3.5 3.5L14 5.5" stroke="#fff" stroke-width="2.4" fill="none"/></svg>Diabetes Foot Assessments</li>
    <li><svg width="18" height="18" viewBox="0 0 18 18"><rect width="18" height="18" rx="3" fill="#8cc63f"/><path d="M4 9l3.5 3.5L14 5.5" stroke="#fff" stroke-width="2.4" fill="none"/></svg>Foot and ankle pain</li>
    <li><svg width="18" height="18" viewBox="0 0 18 18"><rect width="18" height="18" rx="3" fill="#8cc63f"/><path d="M4 9l3.5 3.5L14 5.5" stroke="#fff" stroke-width="2.4" fill="none"/></svg>Flat Feet- Both adults and children</li>
    <li><svg width="18" height="18" viewBox="0 0 18 18"><rect width="18" height="18" rx="3" fill="#8cc63f"/><path d="M4 9l3.5 3.5L14 5.5" stroke="#fff" stroke-width="2.4" fill="none"/></svg>Ingrown nails</li>
    <li><svg width="18" height="18" viewBox="0 0 18 18"><rect width="18" height="18" rx="3" fill="#8cc63f"/><path d="M4 9l3.5 3.5L14 5.5" stroke="#fff" stroke-width="2.4" fill="none"/></svg>Corns/Callus</li>
  </ul>

  <div class="locations-band"></div>
  <h2 class="locations-title">3 Handy locations</h2>

  <div class="location loc-a">
    <h3>Riverbend Medical Centre</h3>
    <span class="label">Place:</span>
    Level 1, 14 Marlow Lane Eastbrook
    <span class="phone">Ph: 9000 1234</span>
  </div>
  <div class="location loc-b">
    <h3>Riverbend Rehabilitation:</h3>
    <span class="label">Place:</span>
    52 Kestrel Street Eastbrook
    <span class="phone">Ph: 9000 5678</span>
  </div>
  <div class="location loc-c">
    <h3>Family Care Hub:</h3>
    <div class="row"><span class="label">Place:</span><span class="phone" style="margin:0">Ph: 9000 4321</span></div>
    20 Marlow Lane Eastbrook
  </div>

  <p class="fine-print">To take advantage of these offers you need to call and make the appointment before 31st December 2018. (*Limited spots available.)<strong>Ph: 9000 4321</strong></p>

  <div class="offer-panel">
    <svg width="429" height="800" viewBox="0 0 429 800"><path d="M0 140 C120 60 260 0 429 20 L429 800 L0 800 Z" fill="#0c3566"/></svg>
  </div>
  <div class="foot-photo" role="img" aria-label="Podiatrist examining a patient's foot"></div>

  <h2 class="offer-title">Special Offer!</h2>
  <p class="offer-intro">We are offering a special price to celebrate the opening of our new location at the Family Care Hub.</p>

  <div class="offer-one">
    <span class="tag">OFFER 1:</span>
    <span class="text"><span class="price">$40</span> Initial appointments. Full assessment and treatment.</span>
  </div>

  <p class="offer-two-text">FREE BIOMECHECNICAL ASSESSMENT</p>
  <div class="offer-two-badge">OFFER 2:</div>

  <p class="worry">Worried about your or your Children's flat feet or painful feet?</p>
  <p class="book">Book in now for an obligation free assessment.</p>
</div>
</body>
</html>
```